Brightmoor Auto Care 4x9 Rack Card

Design a 4" wide by 9" tall rack card printed front and back using the copy, logo and images uploaded below. I am also uploading a current flyer so you can see the typestyles we use. I will get the exact name of the font for you ASAP. Also will be uploading some before and after pictures for the back of the rack card

Target Market(s)

Affluent consumers who need their car cleaned and detailed in a meticulous fashion

Requirements
Must have
• Under the logo, put the words...... Premium Steam Detailing & Ceramic Coating.........also put ther following wording on the front side: Get Steamed! We use steam to clean your vehicle helping save millions of gallons of water and protecting our rivers, streams and lakes from runoff.
Nice to have
• a screened back background of hexagons might be nice

```html
<!DOCTYPE html>
<html lang="en">
<head>
<meta charset="utf-8">
<title>Brightmoor Auto Care Rack Card</title>
<link rel="stylesheet" href="https://fonts.googleapis.com/css2?family=Archivo+Black&family=Arimo:wght@400;700&family=Open+Sans:ital,wght@0,400;0,600;0,700;1,700&display=swap">
<style>
  :root {
    --green: #3a7d35;
    --green-dark: #2f6a2c;
    --blue: #1e4a9c;
    --blue-text: #2b4a9a;
    --ink: #222;
    --paper: #ffffff;
    --stage: #e3e3e3;
    --photo-dark: #2c2f33;
    --photo-mid: #7c848c;
  }
  html, body {
    margin: 0;
    width: 697px;
    height: 1200px;
    overflow: hidden;
    background: var(--stage);
  }
  .rack-card {
    position: absolute;
    top: 250px;
    width: 320px;
    height: 698px;
    box-shadow: 4px 6px 12px rgba(0,0,0,.18);
    background: var(--paper);
  }
  .rack-card--front { left: 20px; }
  .rack-card--back { left: 357px; }
  .rack-card svg { display: block; width: 100%; height: 100%; }
  .fill-green { fill: var(--green); }
  .fill-blue { fill: var(--blue); }
  .fill-white { fill: var(--paper); }
  .brand-name { font-family: "Open Sans", sans-serif; font-weight: 600; fill: var(--green); letter-spacing: 2px; }
  .headline { font-family: "Archivo Black", sans-serif; fill: var(--green-dark); }
  .subhead { font-family: "Arimo", sans-serif; }
  .subhead--blue { fill: var(--blue-text); }
  .subhead--green { fill: var(--green-dark); }
  .body-copy { font-family: "Open Sans", sans-serif; fill: var(--ink); }
  .lead-in { fill: #4a78c2; font-weight: 700; }
  .small-copy { font-family: "Open Sans", sans-serif; fill: var(--ink); }
  .contact { font-family: "Open Sans", sans-serif; fill: var(--paper); }
  .badge-text { font-family: "Arimo", sans-serif; font-weight: 700; fill: var(--paper); text-anchor: middle; }
  .service-title { font-family: "Open Sans", sans-serif; font-weight: 700; fill: var(--blue-text); }
  .service-desc { font-family: "Open Sans", sans-serif; fill: var(--ink); }
  .price { font-family: "Arimo", sans-serif; font-weight: 700; fill: var(--paper); }
  .side-label { font-family: "Open Sans", sans-serif; font-weight: 700; fill: var(--green-dark); }
  .photo-label { font-family: "Open Sans", sans-serif; font-style: italic; font-weight: 700; fill: var(--paper); text-anchor: middle; }
  .closing { font-family: "Arimo", sans-serif; fill: var(--paper); }
</style>
</head>
<body>

<!-- Front side -->
<div class="rack-card rack-card--front">
<svg viewBox="0 0 477 1040" xmlns="http://www.w3.org/2000/svg">
  <defs>
    <linearGradient id="photoFront" x1="0" y1="0" x2="0" y2="1">
      <stop offset="0" stop-color="#3a3a34"/>
      <stop offset=".55" stop-color="#5a6470"/>
      <stop offset="1" stop-color="#1c1f24"/>
    </linearGradient>
  </defs>
  <g role="img" aria-label="Photo of a detailer in a blue shirt hand-polishing the hood of a silver sports car in a garage">
    <polygon points="28,0 477,0 477,520 28,320" fill="url(#photoFront)"/>
  </g>
  <polygon class="fill-green" points="55,335 477,530 477,575 55,380"/>
  <polygon class="fill-blue" points="425,575 477,548 477,612"/>

  <!-- brand -->
  <circle cx="42" cy="493" r="13" class="fill-green"/>
  <text class="brand-name" x="62" y="488" font-size="13">BRIGHTMOOR</text>
  <text class="brand-name" x="62" y="503" font-size="11">AUTO CARE</text>

  <text class="headline" x="28" y="575" font-size="46">PREMIUM</text>
  <text class="subhead subhead--blue" x="28" y="603" font-size="23">STEAM DETAILING &amp;</text>
  <text class="subhead subhead--green" x="28" y="634" font-size="29">CERAMIC COATING</text>
  <rect x="28" y="646" width="86" height="3" class="fill-blue" opacity=".8"/>

  <text class="body-copy" font-size="15.5">
    <tspan x="28" y="676"><tspan class="lead-in">Get Steamed!</tspan> We use steam to clean your vehicle</tspan>
    <tspan x="28" y="695">helping save millions of gallons of water and protecting</tspan>
    <tspan x="28" y="714">our rivers, streams and lakes from runoff.</tspan>
  </text>

  <!-- pin icon + rule -->
  <polygon class="fill-blue" points="43,742 52,747 52,757 43,762 34,757 34,747"/>
  <circle cx="43" cy="751" r="3" class="fill-white"/>
  <line x1="60" y1="752" x2="445" y2="752" stroke="#333" stroke-width="1.2" stroke-dasharray="6 3"/>

  <text class="small-copy" font-size="12.5">
    <tspan x="33" y="788">1420 Larch Avenue @ The Larch Street Commons Brightmoor</tspan>
    <tspan x="33" y="810">52 Cedar Lane Pinecrest Village</tspan>
    <tspan x="33" y="832">308 Halden Rd #112 Ridgeview</tspan>
  </text>

  <!-- bottom bands -->
  <polygon class="fill-blue" points="0,880 55,912 0,940"/>
  <polygon class="fill-blue" points="125,888 150,880 400,1040 360,1040"/>
  <polygon class="fill-green" points="0,950 110,895 340,1040 0,1040"/>

  <!-- phone icon -->
  <circle cx="43" cy="947" r="9" class="fill-white"/>
  <path d="M39 942 l3 0 l1 3 l-2 1 q1 3 4 4 l1-2 l3 1 l0 3 q-8 0 -10-10 z" class="fill-green"/>
  <text class="contact" font-size="12">
    <tspan x="33" y="992">Brightmoor  (555) 214-0187</tspan>
    <tspan x="33" y="1007">Ridgeview  (555) 306-4410</tspan>
    <tspan x="33" y="1022">Pinecrest/Alder (555) 230-7722</tspan>
  </text>

  <!-- badge -->
  <polygon class="fill-green" points="378,833 449,874 449,956 378,997 307,956 307,874"/>
  <polygon points="378,843 440,879 440,951 378,987 316,951 316,879" fill="none" stroke="#fff" stroke-width="2"/>
  <text class="badge-text" font-size="21">
    <tspan x="378" y="887">Fall In</tspan>
    <tspan x="378" y="909">Love With</tspan>
    <tspan x="378" y="931">Your Car</tspan>
    <tspan x="378" y="953">Again!</tspan>
  </text>
</svg>
</div>

<!-- Back side -->
<div class="rack-card rack-card--back">
<svg viewBox="0 0 477 1040" xmlns="http://www.w3.org/2000/svg">
  <defs>
    <linearGradient id="photoBack" x1="0" y1="0" x2="1" y2="1">
      <stop offset="0" stop-color="#6f757b"/>
      <stop offset=".5" stop-color="#2e3236"/>
      <stop offset="1" stop-color="#8a9096"/>
    </linearGradient>
    <linearGradient id="detailPhoto" x1="0" y1="0" x2="1" y2="1">
      <stop offset="0" stop-color="var(--photo-mid)"/>
      <stop offset="1" stop-color="var(--photo-dark)"/>
    </linearGradient>
  </defs>
  <g role="img" aria-label="Photo of a car interior with steering wheel and dashboard">
    <polygon points="0,0 477,0 477,40 0,245" fill="url(#photoBack)"/>
  </g>
  <polygon class="fill-green" points="0,245 420,65 420,95 0,280"/>
  <polygon class="fill-blue" points="0,262 52,290 0,315"/>
  <ellipse cx="420" cy="230" rx="110" ry="80" fill="#dfeedd" opacity=".7"/>

  <!-- brand -->
  <circle cx="306" cy="226" r="13" class="fill-green"/>
  <text class="brand-name" x="326" y="221" font-size="13">BRIGHTMOOR</text>
  <text class="brand-name" x="326" y="236" font-size="11">AUTO CARE</text>

  <!-- service list -->
  <line x1="36" y1="362" x2="36" y2="800" stroke="#555" stroke-width="1.2" stroke-dasharray="2 3"/>
  <g class="fill-blue">
    <polygon points="36,352 45,357 45,367 36,372 27,367 27,357"/>
    <polygon points="36,460 45,465 45,475 36,480 27,475 27,465"/>
    <polygon points="36,569 45,574 45,584 36,589 27,584 27,574"/>
    <polygon points="36,695 45,700 45,710 36,715 27,710 27,700"/>
    <polygon points="36,790 45,795 45,805 36,810 27,805 27,795"/>
  </g>

  <text class="service-title" x="54" y="367" font-size="15">Premium Steam</text>
  <text class="service-desc" x="54" y="386" font-size="15">Washes starting</text>
  <text class="service-desc" x="54" y="416" font-size="15">at</text>
  <polygon class="fill-green" points="77,396 133,396 143,408 133,420 77,420"/>
  <text class="price" x="82" y="416" font-size="21"><tspan font-size="12" dy="-8">$</tspan><tspan dy="8">100</tspan></text>
  <text class="service-desc" x="146" y="416" font-size="15">and up</text>

  <text class="service-title" x="54" y="475" font-size="15">Full Steam</text>
  <text class="service-desc" x="54" y="494" font-size="15">Detailing starting</text>
  <text class="service-desc" x="54" y="526" font-size="15">at</text>
  <polygon class="fill-green" points="77,506 133,506 143,518 133,530 77,530"/>
  <text class="price" x="82" y="526" font-size="21"><tspan font-size="12" dy="-8">$</tspan><tspan dy="8">275</tspan></text>
  <text class="service-desc" x="148" y="526" font-size="15">and up</text>

  <text class="service-title" x="54" y="584" font-size="15">Paint Correction</text>
  <text class="service-desc" x="54" y="603" font-size="15">(multi-stage polishing)</text>
  <text class="service-desc" x="54" y="622" font-size="15">starting</text>
  <text class="service-desc" x="54" y="652" font-size="15">at</text>
  <polygon class="fill-green" points="77,632 133,632 143,644 133,656 77,656"/>
  <text class="price" x="82" y="652" font-size="21"><tspan font-size="12" dy="-8">$</tspan><tspan dy="8">650</tspan></text>
  <text class="service-desc" x="146" y="652" font-size="15">and up</text>

  <text class="service-title" x="54" y="710" font-size="15">Headlight Restoration -</text>
  <polygon class="fill-green" points="77,724 133,724 143,736 133,748 77,748"/>
  <text class="price" x="82" y="744" font-size="21"><tspan font-size="12" dy="-8">$</tspan><tspan dy="8">110</tspan></text>

  <text class="service-title" x="54" y="805" font-size="15">Engine Steam Cleaning -</text>
  <polygon class="fill-green" points="77,817 133,817 143,829 133,841 77,841"/>
  <text class="price" x="82" y="837" font-size="21"><tspan font-size="12" dy="-8">$</tspan><tspan dy="8">75</tspan></text>

  <!-- before / after hexagons -->
  <text class="side-label" font-size="17" transform="translate(289 440) rotate(-90)">Interior</text>
  <text class="side-label" font-size="17" transform="translate(293 680) rotate(-90)">Exterior</text>

  <polygon class="fill-blue" points="370,318 441,359 441,441 370,482 299,441 299,359"/>
  <polygon role="img" aria-label="After photo of a cleaned car interior" points="370,334 427,367 427,433 370,466 313,433 313,367" fill="url(#detailPhoto)"/>
  <text class="photo-label" x="362" y="444" font-size="13">After</text>

  <polygon class="fill-green" points="296,462 355,496 355,564 296,598 237,564 237,496"/>
  <polygon role="img" aria-label="Before photo of a dirty car interior floor" points="296,475 344,502 344,558 296,585 248,558 248,502" fill="url(#detailPhoto)"/>
  <text class="photo-label" x="290" y="572" font-size="13">Before</text>

  <polygon class="fill-blue" points="380,563 451,604 451,686 380,727 309,686 309,604"/>
  <polygon role="img" aria-label="After photo of a cleaned engine bay" points="380,579 437,612 437,678 380,711 323,678 323,612" fill="url(#detailPhoto)"/>
  <text class="photo-label" x="372" y="690" font-size="13">After</text>

  <polygon class="fill-green" points="335,707 394,741 394,809 335,843 276,809 276,741"/>
  <polygon role="img" aria-label="Before photo of a dirty engine bay" points="335,720 383,747 383,803 335,830 287,803 287,747" fill="url(#detailPhoto)"/>
  <text class="photo-label" x="330" y="818" font-size="13">Before</text>

  <!-- bottom bands -->
  <polygon class="fill-blue" points="0,862 75,900 0,935"/>
  <polygon class="fill-blue" points="95,895 120,885 400,1040 355,1040"/>
  <polygon class="fill-green" points="0,1040 0,948 100,895 330,1040"/>
  <text class="closing" font-size="19" font-weight="700">
    <tspan x="33" y="937">CERAMIC</tspan>
    <tspan x="33" y="959">COATING -</tspan>
  </text>
  <text class="closing" font-size="19">
    <tspan x="33" y="983">Call or visit us for</tspan>
    <tspan x="33" y="1005">a Quote</tspan>
  </text>

  <!-- badge -->
  <polygon class="fill-green" points="380,833 451,874 451,956 380,997 309,956 309,874"/>
  <polygon points="380,843 442,879 442,951 380,987 318,951 318,879" fill="none" stroke="#fff" stroke-width="2"/>
  <text class="badge-text" font-size="21">
    <tspan x="380" y="887">Fall In</tspan>
    <tspan x="380" y="909">Love With</tspan>
    <tspan x="380" y="931">Your Car</tspan>
    <tspan x="380" y="953">Again!</tspan>
  </text>
</svg>
</div>

</body>
</html>
```